【重要事項】
ワードプレスでのホームページ制作依頼、別途予定あり
デザインから制作まで一貫して行える方はご相談ください。
トップページデザインのみのご提案ももちろん大歓迎です。

【トップページデザインの要望】
・コンパクトでユーザーフレンドリー、お客様を意識したトップページ
サイトを訪れた人が求める情報にすぐアクセスできるデザインを希望します。詳細は添付ファイルをご覧ください。

【弊社ホームページ】
リニューアル対象のホームページURLのほか下記
http://kumoyama-shop.jp/
園芸のECサイトです。

【添付ファイル】
共有事項は添付ファイルにまとめています。お手数ですがご一読ください。
ロゴもございます。デザイン作成にお役立てください。
サイトURL
http://kumoyama.jp/
ページ数
1ページ
希望イメージ
シンプル 複雑
単色 カラフル
暗い 明るい
日常 高級
遊び心 厳粛
未来的 伝統的
女性的 男性的
希望する色
緑系
納品ファイル
• 高解像度JPG (.jpg)
• PNG形式 (.png)
補足説明
8/31追記(質問への回答まとめ)

【納品形式の追加】
ai形式/PSD形式の納品可
※要望には個別でも柔軟に対応します。

【ロゴデータの追加】
pngデータ2つ、jpgデータ1つ
色のこだわりは強くありません。デザインに合わせてご活用ください。

【参考にしたいサイト】
https://q-r.co.jp/
最近できた会社様で、お客様目線に振り切ったデザインです。
ここまでポップにはできませんが、取り入れられる要素は取り入れたいと思っています。

https://www.mira-vento.com/
競合他社様ですが、多言語対応できるデザインレイアウトが印象的です。
弊社も英語対応のホームページ(弊社にて文言を翻訳)にする予定です。

みなさまのご応募お待ちしております。
■ 選んだ理由

当選者:杉本様
当選理由:社内会議による選考の末、多数決により決定しました。
色合いとデザインの段組が非常に優れておりました。
次点入選:marble様、rui様
入選理由:marble様は社内会議で最後まで当選作品と一、二を争う優秀作品でした。
特にイラストのテイストが社長の好みに合っており好印象でした。
rui様は写真の選定センス、全体のデザイン感が女性社員に受けました。

■ 提案者全員のお礼・コメント

今回は担当が変わってから初めての提案でした。
不慣れなことが多い中、たくさんのご提案をいただき、様々な改善点や面白いデザイン、よりよいHPづくりのヒントをワーカルのエキスパートの皆様よりいただきました。
誠にお礼申し上げます。

また、後半ご提出のご提案には、逐一ご挨拶ができず申し訳ございませんでした。
今回いただけた縁を活かして、よりよいHP制作につなげていきたいと考えております。

惜しくも当選、入選とならなかった皆様にも、心よりお礼を申し上げます。
またの機会がございましたら、よろしくお願いします。

```html
<!DOCTYPE html>
<html lang="ja">
<head>
<meta charset="utf-8">
<title>くもやま産業</title>
<link href="https://fonts.googleapis.com/css2?family=Noto+Sans+JP:wght@400;500;700;900&family=Montserrat:wght@600;700;800&display=swap" rel="stylesheet">
<style>
:root{
  --green:#1f9a3a;
  --green-dark:#0f7a2e;
  --green-deep:#0b6426;
  --lime:#c6e02a;
  --yellow:#f3cf12;
  --orange:#f08a1c;
  --ink:#333;
  --muted:#777;
  --white:#fff;
}
*{box-sizing:border-box;margin:0;padding:0}
html,body{width:1200px;height:2288px;overflow:hidden}
body{font-family:"Noto Sans JP",sans-serif;color:var(--ink);background:var(--white);position:relative}

/* header */
.site-header{position:absolute;top:0;left:0;width:1200px;height:44px;background:var(--white);border-bottom:3px solid var(--green)}
.brand{position:absolute;left:40px;top:5px;font-size:17px;font-weight:700;color:var(--green-dark);line-height:1}
.brand-sub{position:absolute;left:40px;top:27px;font-size:7px;color:var(--muted)}
.global-nav{position:absolute;left:320px;top:8px;display:flex;gap:4px}
.global-nav a{display:block;width:86px;height:30px;background:var(--green);color:var(--white);font-size:9px;font-weight:700;text-decoration:none;padding:4px 6px;line-height:1.2}
.global-nav a span{display:block;font-size:6px;font-weight:400;opacity:.85}
.header-contact{position:absolute;right:40px;top:6px;text-align:right;font-size:8px;color:var(--green-dark)}
.header-contact .tag{display:inline-block;background:var(--green);color:#fff;padding:1px 6px;margin-bottom:3px}

/* hero */
.hero{position:absolute;top:44px;left:0;width:1200px;height:330px;background:linear-gradient(120deg,#7a8c6a 0%,#b9c3a8 30%,#c9d6c0 55%,#6f8a5a 80%,#3f5a3a 100%);overflow:hidden}
.hero-diamond{position:absolute;left:700px;top:40px;width:250px;height:250px}
.hero-copy{position:absolute;left:720px;top:108px;width:210px;text-align:center}
.hero-copy h1{font-size:18px;font-weight:900;color:var(--green);line-height:1.5;white-space:nowrap}
.hero-copy p{font-size:7px;color:var(--muted);margin-top:8px;line-height:1.6}

/* entry cards */
.entry-card{position:absolute;top:370px;width:285px;height:110px;background:var(--white);border:3px solid var(--yellow);box-shadow:0 2px 6px rgba(0,0,0,.12);padding:12px 14px}
.entry-card h2{font-size:15px;font-weight:900;color:var(--green-dark);line-height:1.35;width:150px}
.entry-card ul{list-style:none;font-size:7px;color:var(--muted);margin-top:8px;line-height:1.6;width:150px}
.entry-card .thumb{position:absolute;right:10px;top:10px;width:100px;height:84px}
.entry-card .more{position:absolute;left:14px;bottom:8px;font-size:7px;background:var(--green);color:#fff;padding:1px 8px}

/* news */
.news{position:absolute;top:500px;left:0;width:1200px;height:260px}
.news-head{position:absolute;left:200px;top:35px;display:flex;align-items:baseline;gap:14px}
.news-head h2{font-family:"Montserrat",sans-serif;font-weight:800;font-size:24px;color:var(--green)}
.news-head span{font-size:8px;color:var(--muted)}
.news-rule{position:absolute;left:200px;top:72px;width:800px;height:2px;background:var(--green)}
.news-grid{position:absolute;left:200px;top:88px;display:flex;gap:12px}
.news-card{width:191px}
.news-card .photo{height:86px}
.news-card .label{background:var(--green);color:#fff;font-size:9px;font-weight:700;padding:3px 8px}
.news-card p{font-size:7px;color:var(--muted);line-height:1.5;margin-top:4px}
.news-all{position:absolute;right:200px;top:36px;font-size:8px;border:1px solid var(--green);color:var(--green);padding:3px 12px}

/* company */
.company{position:absolute;top:780px;left:0;width:1200px;height:230px;background:var(--lime)}
.company h2{position:absolute;left:240px;top:50px;font-size:26px;font-weight:900;color:var(--green-deep);line-height:1.4}
.company p{position:absolute;left:240px;top:140px;width:300px;font-size:8px;color:#4a5a1a;line-height:1.6}
.btn{display:inline-block;background:var(--white);color:var(--green-dark);font-size:8px;font-weight:700;padding:6px 16px;border-radius:2px}
.company .btn{position:absolute;left:240px;top:180px}
.company .photo{position:absolute;left:590px;top:15px;width:330px;height:200px;box-shadow:0 4px 10px rgba(0,0,0,.15)}

/* bases */
.bases{position:absolute;top:1010px;left:0;width:1200px;height:230px;background:var(--green)}
.bases .field{position:absolute;left:0;top:0;width:240px;height:230px}
.bases h2{position:absolute;left:270px;top:55px;font-size:26px;font-weight:900;color:var(--white);line-height:1.4}
.bases p{position:absolute;left:270px;top:145px;width:300px;font-size:8px;color:#d8f0d8;line-height:1.6}
.bases .map{position:absolute;left:700px;top:15px;width:210px;height:200px}
.bases .btn{position:absolute;left:880px;top:190px}

/* recruit */
.recruit{position:absolute;top:1240px;left:0;width:1200px;height:350px;background:var(--white)}
.sec-title{position:absolute;left:0;width:1200px;text-align:center}
.sec-title h2{font-size:20px;font-weight:900;color:var(--green-dark)}
.sec-title span{display:block;font-family:"Montserrat",sans-serif;font-size:9px;color:var(--green);margin-top:2px}
.recruit .sec-title{top:40px}
.recruit .photo{position:absolute;left:330px;top:100px;width:350px;height:200px}
.recruit .box{position:absolute;left:680px;top:110px;width:210px;height:140px;background:var(--green);padding:22px 20px;color:#fff}
.recruit .box h3{font-size:13px;font-weight:700;line-height:1.5}
.recruit .box p{font-size:7px;line-height:1.6;margin-top:8px;opacity:.9}
.recruit .photo2{position:absolute;left:700px;top:250px;width:190px;height:70px}

/* interview */
.interview{position:absolute;top:1590px;left:0;width:1200px;height:330px;background:linear-gradient(#fbfde8,#eef6c4)}
.interview .sec-title{top:28px}
.interview .lead{position:absolute;left:0;top:80px;width:1200px;text-align:center;font-size:8px;color:var(--muted)}
.staff{position:absolute;top:120px;width:120px;text-align:center}
.staff svg{display:block;margin:0 auto}
.staff .role{display:inline-block;margin-top:10px;font-size:11px;font-weight:700;color:var(--green-dark);border-bottom:2px solid var(--green);padding:0 6px}
.staff.orange .role{color:var(--orange);border-color:var(--orange)}
.staff p{font-size:7px;color:var(--muted);margin-top:6px}

/* footer */
.site-footer{position:absolute;top:1920px;left:0;width:1200px;height:368px;background:var(--green);color:#fff}
.footer-brand{position:absolute;left:110px;top:26px;font-size:14px;font-weight:700}
.footer-top{position:absolute;left:110px;top:66px;font-size:9px;font-weight:700}
.footer-cols{position:absolute;left:110px;top:92px;display:flex;gap:40px}
.footer-cols ul{list-style:none;width:160px;font-size:8px;line-height:2.1}
.footer-cols li:first-child{font-weight:700;border-bottom:1px solid rgba(255,255,255,.4);margin-bottom:2px}
.footer-tel{position:absolute;left:110px;top:240px;font-size:13px;font-weight:700}
.footer-tel small{display:block;font-size:8px;font-weight:400}
.footer-addr{position:absolute;left:330px;top:244px;font-size:8px;line-height:1.7}
.copyright{position:absolute;left:0;bottom:0;width:1200px;height:30px;background:var(--green-deep);text-align:center;font-size:7px;line-height:30px}
</style>
</head>
<body>

<header class="site-header">
  <div class="brand">くもやま産業</div>
  <div class="brand-sub">動物と植物の専門商社</div>
  <nav class="global-nav">
    <a href="#">会社について<span>ABOUT US</span></a>
    <a href="#">取扱商品<span>PRODUCTS</span></a>
    <a href="#">拠点紹介<span>OFFICES</span></a>
    <a href="#">採用情報<span>RECRUIT</span></a>
    <a href="#">お知らせ<span>NEWS</span></a>
    <a href="#">お問合せ<span>CONTACT</span></a>
  </nav>
  <div class="header-contact"><span class="tag">お問合せ</span><br>TEL 0120-48-2736</div>
</header>

<section class="hero" role="img" aria-label="社員や牛、植物の写真をひし形に並べたコラージュ">
  <svg class="hero-diamond" viewBox="0 0 250 250"><rect x="37" y="37" width="176" height="176" fill="#fff" transform="rotate(45 125 125)"/></svg>
  <div class="hero-copy">
    <h1>動物や植物を通して<br>豊かな生活を。</h1>
    <p>私たちは畜産と園芸の分野で<br>人と自然をつなぐ商品と<br>サービスをお届けします。</p>
  </div>
</section>

<a class="entry-card" style="left:305px">
  <h2>畜産・動物用<br>商品はこちら</h2>
  <ul><li>飼料・動物用医薬品</li><li>畜産資材・機器</li></ul>
  <div class="thumb" role="img" aria-label="牛の写真" style="background:linear-gradient(#a8b48c,#5d6a43)"></div>
  <span class="more">詳しく見る</span>
</a>
<a class="entry-card" style="left:610px">
  <h2>農業・園芸用品の<br>卸事業はこちら</h2>
  <ul><li>肥料・園芸資材</li><li>種苗・農業機器</li></ul>
  <div class="thumb" role="img" aria-label="鉢植えの植物の写真" style="background:linear-gradient(#d9e6b8,#7a9a4a)"></div>
  <span class="more">詳しく見る</span>
</a>

<section class="news">
  <div class="news-head"><h2>NEWS</h2><span>お知らせ　イベント情報　商品情報　採用情報</span></div>
  <span class="news-all">一覧を見る</span>
  <div class="news-rule"></div>
  <div class="news-grid">
    <article class="news-card"><div class="photo" role="img" aria-label="新商品の写真" style="background:linear-gradient(#e8dcc0,#b89a6a)"></div><div class="label">新商品のお知らせ</div><p>2018.09.01 春の園芸資材が入荷しました。</p></article>
    <article class="news-card"><div class="photo" role="img" aria-label="食品の写真" style="background:linear-gradient(#f0e2c8,#c9a06a)"></div><div class="label">イベント情報</div><p>2018.08.24 展示会に出展いたします。</p></article>
    <article class="news-card"><div class="photo" role="img" aria-label="野菜の写真" style="background:linear-gradient(#e4ecc8,#9aab6a)"></div><div class="label">商品情報</div><p>2018.08.10 飼料の価格改定について。</p></article>
    <article class="news-card"><div class="photo" role="img" aria-label="店舗の写真" style="background:linear-gradient(#ece4d4,#b0a080)"></div><div class="label">採用情報</div><p>2018.08.01 新卒採用を開始しました。</p></article>
  </div>
</section>

<section class="company">
  <h2>人に本当に選ばれる<br>企業を目指して</h2>
  <p>創業以来、お客様の声に耳を傾け、確かな品質と誠実な対応でお応えしてきました。</p>
  <span class="btn">会社の紹介・代表メッセージ　›</span>
  <div class="photo" role="img" aria-label="オフィスに立つ代表者の写真" style="background:linear-gradient(120deg,#d8dcd8,#8f9a98)"></div>
</section>

<section class="bases">
  <div class="field" role="img" aria-label="牧場で草を食む牛の写真" style="background:linear-gradient(#4e8a3e,#2d5a22)"></div>
  <h2>関東・北海道を中心に<br>広がる当社の拠点</h2>
  <p>全国各地の拠点から、地域に根ざした迅速なサービスを提供しています。</p>
  <div class="map" role="img" aria-label="拠点を示す日本地図" style="background:linear-gradient(135deg,rgba(255,255,255,.85),rgba(255,255,255,.6))"></div>
  <span class="btn">拠点一覧を見る　›</span>
</section>

<section class="recruit">
  <div class="sec-title"><h2>採用情報</h2><span>Recruit</span></div>
  <div class="photo" role="img" aria-label="社員の集合写真" style="background:linear-gradient(#c8ccc4,#6e7468)"></div>
  <div class="box"><h3>動物や植物を通して、<br>人の暮らしを支える。</h3><p>私たちと一緒に未来をつくる仲間を募集しています。</p></div>
  <div class="photo2" role="img" aria-label="働く社員の写真" style="background:linear-gradient(#d8d4cc,#8a867a)"></div>
</section>

<section class="interview">
  <div class="sec-title"><h2>社員インタビュー</h2></div>
  <p class="lead">現場で働く社員の声をご紹介します。仕事のやりがいや一日の流れをご覧ください。</p>
  <div class="staff" style="left:330px">
    <svg width="110" height="110" viewBox="0 0 110 110" role="img" aria-label="営業職の社員の写真"><circle cx="55" cy="55" r="52" fill="#fff" stroke="#1f9a3a" stroke-width="5"/><circle cx="55" cy="55" r="44" fill="#9aa39a"/></svg>
    <span class="role">営業職</span><p>入社5年目</p>
  </div>
  <div class="staff" style="left:540px">
    <svg width="110" height="110" viewBox="0 0 110 110" role="img" aria-label="営業職の社員の写真"><circle cx="55" cy="55" r="52" fill="#fff" stroke="#1f9a3a" stroke-width="5"/><circle cx="55" cy="55" r="44" fill="#a39a90"/></svg>
    <span class="role">営業職</span><p>入社3年目</p>
  </div>
  <div class="staff orange" style="left:750px">
    <svg width="110" height="110" viewBox="0 0 110 110" role="img" aria-label="企画職の社員の写真"><circle cx="55" cy="55" r="52" fill="#fff" stroke="#f08a1c" stroke-width="5"/><circle cx="55" cy="55" r="44" fill="#b0a498"/></svg>
    <span class="role">企画職</span><p>入社2年目</p>
  </div>
</section>

<footer class="site-footer">
  <div class="footer-brand">くもやま産業</div>
  <div class="footer-top">トップページ</div>
  <div class="footer-cols">
    <ul><li>会社について</li><li>代表挨拶</li><li>会社概要</li><li>沿革</li></ul>
    <ul><li>取扱商品</li><li>畜産・動物用商品</li><li>農業・園芸用品</li><li>新商品情報</li></ul>
    <ul><li>拠点紹介</li><li>関東エリア</li><li>北海道エリア</li><li>その他の拠点</li></ul>
    <ul><li>採用情報</li><li>社員インタビュー</li><li>募集要項</li><li>お問合せ</li></ul>
  </div>
  <div class="footer-tel">TEL:0120-48-2736<small>FAX:0120-48-2737</small></div>
  <div class="footer-addr">〒000-0000 本社所在地 サンプル町1-2-3<br>受付時間 平日 9:00〜17:00</div>
  <div class="copyright">Copyright © くもやま産業 All Rights Reserved.</div>
</footer>

</body>
</html>
```